Door Hanger Design for Electricians Serving Homes

I would like our logo incorporated into the door hanger. We would like a place for a tear off section on the bottom of the hanger with our contact information: K&T Electric - (555) 318-4702 - www.kandtelectric.example - info@kandtelectric.example.
Door Hanger Script
Front Side of the Door Hanger:
[Company Logo]
Need a Reliable Electrician?
Your Local Electrical Expert is Just Around the Corner!
• Quick Response Times
• Affordable Rates
• Quality Workmanship
• Fully Licensed & Insured
• Special Offer:
• 10% OFF Your First Service Call!
Back Side of the Door Hanger:
Don't Let Electrical Issues Keep You in the Dark!
From flickering lights to complete system upgrades, we've got all your
residential electrical needs covered. Our services include:
• Electrical Repairs & Troubleshooting
• Lighting Installation & Upgrades
• Safety Inspections & Code Compliance
• Energy-Efficient Solutions
• 24/7 Emergency Services
• Why Choose Us?
• Friendly, Local Service
• Over 30 Years of Experience
• Satisfaction Guaranteed
• Upfront Pricing
Call Us Today: [Your Phone Number]
Visit Our Website: [Your Website]
Book Your Appointment Now and Claim Your 10% Discount!
Offer valid for new customers on the first visit only. Mention this door hanger when
booking.
[Your Company Name and Contact Information]
Follow Us on Social Media for More Tips and Special Offers!
[Icons for social media platforms: Chatterpage, Pixmosaic, Quibbler, etc.]
Design Tips:
Use bold, clear fonts for easy reading.
Incorporate your brand colors and logo for instant recognition.
Include a clear call to action (CTA) on both sides.
Add a tear-off section at the bottom with your contact information for
convenience.
Use high-quality images or graphics related to electrical work to catch
the eye.
This door hanger design and copy aim to attract residential clients by
highlighting the benefits of your electrical services, special offers, and
how they can easily get in touch with you for their electrical needs.
The door knocker template will have three of the same design on front and three of the same design on the back. This template is from the print shop.

```html
<!DOCTYPE html>
<html lang="en">
<head>
<meta charset="utf-8">
<title>K&amp;T Electric Door Hanger</title>
<link rel="stylesheet" href="https://fonts.googleapis.com/css2?family=DM+Serif+Display&family=Jost:wght@400;500&family=Oswald:wght@500;600&family=Roboto:wght@400;500&display=swap">
<style>
:root{
  --stage:#5d6063;
  --red:#d71f27;
  --red-deep:#a5141a;
  --ink:#2b2b2b;
  --black:#111;
  --white:#fff;
}
*{margin:0;padding:0;box-sizing:border-box}
html,body{width:1200px;height:1182px;overflow:hidden;background:var(--stage)}
.canvas{position:relative;width:1200px;height:1182px}
.side-label{position:absolute;top:30px;width:200px;margin-left:-100px;text-align:center;color:var(--white);font:700 30px/1 "DM Serif Display",serif}
.hanger{position:absolute;top:75px;overflow:hidden;box-shadow:4px 6px 10px rgba(0,0,0,.35)}
.hanger--front{left:120px;width:444px;height:1021px}
.hanger--back{left:606px;width:445px;height:1025px;background:var(--ink)}
.shapes{position:absolute;left:0;top:0}
.abs{position:absolute}
.center{left:0;right:0;text-align:center}
.brand-mark{position:absolute;border-radius:50%;background:var(--white);border:6px solid var(--red);display:flex;align-items:center;justify-content:center;text-align:center;color:var(--ink);font:400 34px/1.05 "DM Serif Display",serif}
.headline-front{left:40px;top:400px;font:400 47px/50px "DM Serif Display",serif;color:var(--black)}
.headline-front .accent{color:var(--red)}
.tagline{left:41px;top:510px;font:400 15px/1 "Jost",sans-serif;color:var(--ink)}
.perks{left:38px;top:543px;list-style:none}
.perks li{display:flex;align-items:center;height:36.5px;font:400 20px/1 "Jost",sans-serif;color:var(--ink)}
.perks svg{margin-right:6px;flex:none}
.photo{position:absolute;border-radius:8px}
.offer{position:absolute;left:304px;top:593px;width:121px;height:260px;background:var(--red);border-radius:14px 14px 0 0;overflow:hidden;text-align:center;color:var(--white);font-family:"Oswald",sans-serif}
.offer__cap{background:var(--black);height:32px;font:500 19px/32px "Oswald",sans-serif;border-radius:14px 14px 12px 12px}
.offer__big{font:600 64px/62px "Oswald",sans-serif;margin-top:6px;letter-spacing:-1px}
.offer__small{font:500 17px/19px "Oswald",sans-serif;margin-top:4px}
.contact{left:0;right:0;text-align:center;color:var(--white)}
.contact__call{display:flex;align-items:center;justify-content:center;gap:8px;font:500 30px/1 "Oswald",sans-serif}
.contact__lines{margin-top:10px;display:flex;justify-content:center;gap:12px;font:400 14px/1 "Roboto",sans-serif}
.contact__lines span{display:flex;align-items:center;gap:4px}
.contact__follow{margin-top:9px;font:500 10px/1 "Roboto",sans-serif}
.contact__social{margin-top:10px;font:500 11px/1 "Roboto",sans-serif;color:var(--red);display:flex;justify-content:center;gap:10px}
.headline-back{top:270px;font:400 34px/37px "DM Serif Display",serif;color:var(--white)}
.intro{top:385px;font:400 15px/18px "Roboto",sans-serif;color:var(--white)}
.panel{position:absolute;top:440px;width:187px;height:208px;background:linear-gradient(160deg,var(--red),#c3181f 60%,var(--red));border-radius:14px;color:var(--white)}
.panel__tab{position:absolute;top:0;left:32px;width:110px;height:22px;background:var(--black);border-radius:0 0 10px 10px;text-align:center;font:400 13px/22px "DM Serif Display",serif}
.panel ul{list-style:none;position:absolute;top:33px;left:15px;right:8px}
.panel li{position:relative;padding-left:13px;font:400 12.5px/15px "Jost",sans-serif;margin-bottom:9px}
.panel li::before{content:"";position:absolute;left:1px;top:4px;width:6px;height:6px;border:1.3px solid var(--white);transform:rotate(45deg)}
.book{top:738px;font:500 30px/1 "Oswald",sans-serif;color:var(--ink);letter-spacing:-.3px}
.claim{position:absolute;left:108px;top:773px;width:232px;height:24px;border-radius:6px;background:var(--red);color:var(--white);text-align:center;font:500 17px/24px "Oswald",sans-serif}
.fineprint{top:803px;font:400 10px/12.5px "Jost",sans-serif;color:var(--ink)}
</style>
</head>
<body>
<main class="canvas">
  <h2 class="side-label" style="left:352px">FRONT</h2>
  <h2 class="side-label" style="left:831px">BACK</h2>

  <!-- Front side -->
  <section class="hanger hanger--front">
    <svg class="shapes" width="444" height="1021" viewBox="0 0 444 1021">
      <defs>
        <linearGradient id="redRoom" x1="0" y1="0" x2="1" y2="1">
          <stop offset="0" stop-color="#e0262b"/><stop offset=".6" stop-color="#a8141a"/><stop offset="1" stop-color="#6e0d10"/>
        </linearGradient>
      </defs>
      <rect width="444" height="440" fill="url(#redRoom)" role="img" aria-label="Red-tinted photo of a modern kitchen and dining room with pendant lights"/>
      <circle cx="223" cy="138" r="62" fill="var(--black)"/>
      <path d="M0,345 Q110,245 230,262 L230,300 Q110,290 0,372 Z" fill="var(--ink)"/>
      <path d="M0,372 Q120,290 230,300 Q340,320 444,400 L444,1021 L0,1021 Z" fill="var(--white)"/>
      <path d="M0,800 Q230,890 444,806 L444,835 Q230,925 0,828 Z" fill="var(--red)"/>
      <path d="M0,812 Q230,905 444,822 L444,1021 L0,1021 Z" fill="var(--ink)"/>
    </svg>

    <div class="brand-mark" style="left:130px;top:216px;width:186px;height:186px">K&amp;T<br>Electric</div>

    <h1 class="abs headline-front">Need a <span class="accent">Reliable</span><br><span class="accent">Electrician?</span></h1>
    <p class="abs tagline">Your Local Electrical Expert is Just Around the Corner!</p>

    <ul class="abs perks">
      <li><svg width="32" height="32" viewBox="0 0 32 32"><circle cx="16" cy="16" r="16" fill="var(--ink)"/><circle cx="16" cy="16" r="8" fill="none" stroke="#fff" stroke-width="1.6"/><path d="M16 11v5l3 2" stroke="#fff" stroke-width="1.6" fill="none"/></svg>Quick Response Times</li>
      <li><svg width="32" height="32" viewBox="0 0 32 32"><circle cx="16" cy="16" r="16" fill="var(--ink)"/><text x="16" y="21" text-anchor="middle" fill="#fff" font-family="Roboto,sans-serif" font-size="15">$</text></svg>Affordable Rates</li>
      <li><svg width="32" height="32" viewBox="0 0 32 32"><circle cx="16" cy="16" r="16" fill="var(--ink)"/><path d="M10 16l4 4 8-8" stroke="#fff" stroke-width="2" fill="none"/></svg>Quality Workmanship</li>
      <li><svg width="32" height="32" viewBox="0 0 32 32"><circle cx="16" cy="16" r="16" fill="var(--ink)"/><path d="M16 8l7 3v5c0 4-3 7-7 8-4-1-7-4-7-8v-5z" stroke="#fff" stroke-width="1.6" fill="none"/></svg>Fully Licensed &amp; Insured</li>
    </ul>

    <div class="photo" style="left:38px;top:701px;width:122px;height:96px;background:linear-gradient(135deg,#c9a57a,#8a5a32 60%,#e8e2d8)" role="img" aria-label="Photo of a bright kitchen with wood cabinets"></div>
    <div class="photo" style="left:166px;top:701px;width:123px;height:96px;background:linear-gradient(135deg,#4a4f5a,#7d8896 50%,#c8b18a)" role="img" aria-label="Photo of an electrician wiring a breaker panel"></div>

    <div class="offer">
      <div class="offer__cap">SPECIAL OFFER</div>
      <div class="offer__big">10%<br>OFF</div>
      <div class="offer__small">YOUR FIRST<br>SERVICE CALL!</div>
    </div>

    <div class="abs contact" style="top:896px">
      <div class="contact__call">
        <svg width="32" height="32" viewBox="0 0 32 32"><circle cx="16" cy="16" r="16" fill="var(--red)"/><path d="M11 9l3 1 1 4-2 1c1 2 3 4 5 5l1-2 4 1 1 3-2 2c-6 0-13-7-13-13z" fill="none" stroke="#fff" stroke-width="1.4"/></svg>
        CALL US TODAY (555) 318-4702
      </div>
      <div class="contact__lines">
        <span><svg width="14" height="11" viewBox="0 0 14 11"><rect x=".5" y=".5" width="13" height="10" fill="none" stroke="#fff"/><path d="M.5 .5l6.5 5 6.5-5" fill="none" stroke="#fff"/></svg>info@kandtelectric.example</span>
        <span><svg width="13" height="13" viewBox="0 0 14 14"><circle cx="7" cy="7" r="6" fill="none" stroke="#fff"/><path d="M1 7h12M7 1c-3 3-3 9 0 12M7 1c3 3 3 9 0 12" fill="none" stroke="#fff"/></svg>www.kandtelectric.example</span>
      </div>
      <p class="contact__follow">Follow Us on Social Media for More Tips and Special Offers!</p>
      <p class="contact__social"><span>Chatterpage</span><span>Pixmosaic</span><span>Quibbler</span></p>
    </div>
  </section>

  <!-- Back side -->
  <section class="hanger hanger--back">
    <svg class="shapes" width="445" height="1025" viewBox="0 0 445 1025">
      <defs>
        <linearGradient id="barRoom" x1="0" y1="0" x2="0" y2="1">
          <stop offset="0" stop-color="#d9d3c7"/><stop offset=".55" stop-color="#8a7a5c"/><stop offset="1" stop-color="#e0522e"/>
        </linearGradient>
      </defs>
      <path d="M0,0 H445 V215 Q220,270 0,225 Z" fill="url(#barRoom)" role="img" aria-label="Photo of a brightly lit restaurant bar with shelving and yellow stools"/>
      <circle cx="225" cy="137" r="58" fill="var(--stage)"/>
      <path d="M0,500 Q222,440 445,500 L445,830 Q222,900 0,820 Z" fill="var(--white)"/>
      <path d="M0,818 Q222,895 445,826 L445,848 Q222,920 0,836 Z" fill="var(--red)"/>
    </svg>

    <h1 class="abs center headline-back">Don't Let<br>Electrical Issues Keep<br>You in the Dark!</h1>
    <p class="abs center intro">From flickering lights to complete system upgrades, we've<br>got all your residential electrical needs covered.</p>

    <div class="panel" style="left:35px">
      <div class="panel__tab">Our services</div>
      <ul>
        <li>Electrical Repairs &amp;<br>Troubleshooting</li>
        <li>Lighting Installation &amp;<br>Upgrades</li>
        <li>Safety Inspections &amp;<br>Code Compliance</li>
        <li>Energy-Efficient Solutions</li>
        <li>24/7 Emergency Services</li>
      </ul>
    </div>
    <div class="panel" style="left:228px">
      <div class="panel__tab" style="left:25px;width:124px">Why Choose Us?</div>
      <ul>
        <li>Friendly, Local Service</li>
        <li>Over 30 Years of<br>Experience</li>
        <li>Satisfaction Guaranteed</li>
        <li>Upfront Pricing</li>
      </ul>
    </div>
    <div class="brand-mark" style="left:326px;top:572px;width:104px;height:104px;font-size:19px;border-width:4px">K&amp;T<br>Electric</div>

    <div class="photo" style="left:35px;top:658px;width:123px;height:73px;background:linear-gradient(180deg,#3c4150,#bfc3c8)" role="img" aria-label="Photo of a large lit warehouse interior"></div>
    <div class="photo" style="left:163px;top:658px;width:122px;height:73px;background:linear-gradient(180deg,#2f3240,#d8b46a)" role="img" aria-label="Photo of a modern chandelier in a dark ceiling"></div>
    <div class="photo" style="left:292px;top:658px;width:122px;height:73px;background:linear-gradient(180deg,#e8e8ea,#b8aa95)" role="img" aria-label="Photo of a bright living room with pendant light"></div>

    <p class="abs center book">BOOK YOUR APPOINTMENT NOW</p>
    <div class="claim">AND CLAIM YOUR 10% DISCOUNT!</div>
    <p class="abs center fineprint">Offer valid for new customers on the first visit only.<br>Mention this door hanger when booking.</p>

    <div class="abs contact" style="top:900px">
      <div class="contact__call">
        <svg width="32" height="32" viewBox="0 0 32 32"><circle cx="16" cy="16" r="16" fill="var(--red)"/><path d="M11 9l3 1 1 4-2 1c1 2 3 4 5 5l1-2 4 1 1 3-2 2c-6 0-13-7-13-13z" fill="none" stroke="#fff" stroke-width="1.4"/></svg>
        CALL US TODAY (555) 318-4702
      </div>
      <div class="contact__lines">
        <span><svg width="14" height="11" viewBox="0 0 14 11"><rect x=".5" y=".5" width="13" height="10" fill="none" stroke="#fff"/><path d="M.5 .5l6.5 5 6.5-5" fill="none" stroke="#fff"/></svg>info@kandtelectric.example</span>
        <span><svg width="13" height="13" viewBox="0 0 14 14"><circle cx="7" cy="7" r="6" fill="none" stroke="#fff"/><path d="M1 7h12M7 1c-3 3-3 9 0 12M7 1c3 3 3 9 0 12" fill="none" stroke="#fff"/></svg>www.kandtelectric.example</span>
      </div>
      <p class="contact__follow">Follow Us on Social Media for More Tips and Special Offers!</p>
      <p class="contact__social"><span>Chatterpage</span><span>Pixmosaic</span><span>Quibbler</span></p>
    </div>
  </section>
</main>
</body>
</html>
```